Home Page for Tallyvane

We need to design a new home page for Tallyvane.com, a provider of B2B data for sales and marketing professionals.

The home page should follow the lead of our newly re-designed header and logo (still being tweaked) and use our new color scheme. Please refer to attached file. Please use this file as as the basis of the design for the rest or the home page. No part of the header or logo needs to be altered in this project.

All submissions should be clear, fresh, clean and simple in style. We like the look and feel of ledgerpond.com, tabulryx.com and pollwarren.com. Please use them as references.

The main functions of the home page will be to tell the user about 1) the benefits and uses of Tallyvane and 2) to get them to sign up.

Based upon the successful redesign of our homepage, we will also be redesigning our subscription page and our about us page in the coming weeks.

Target Market(s)

Sales and marketing professionals. Mostly 25 - 45 year old males.

Industry/Entity Type

Marketing

Requirements
Must have
• Items needed:

1A) There should be three main points highlighted 1) Fresh Data 2) Sales Intelligence 3) Increased Bottomline. There will be further text under these headers tbd. For style/feel reference the same device used by pollwarren uses on its homepage.

1B) When you rollover these three items they should highlight and be clickable. The click will lead you to a header and paragraph about each that is further down the homepage (text tbd).

2) We also need a free trial and a sign up button. This button should move with you as you scroll up and down the homepage. Reference www.ledgerpond.com.

3) We need a “Featured In” section. Also reference ledgerpond.com. You can pull the content from tallyvane.com’s current home page.

4) We also need a social media buttons section (facebook, twitter, google+ and linkedIn)

```html
<!DOCTYPE html>
<html lang="en">
<head>
<meta charset="utf-8">
<title>Tallyvane – Create Surveys. Get Answers.</title>
<link href="https://fonts.googleapis.com/css2?family=Montserrat:wght@400;600;700&family=Open+Sans:wght@400;600&display=swap" rel="stylesheet">
<style>
:root{
  --blue:#1a8fe8;
  --blue-dark:#0f7ad0;
  --orange:#f28a1c;
  --green:#7fae1c;
  --green-dark:#5f8a0f;
  --ink:#333;
  --muted:#8a8a8a;
  --charcoal:#2e2e2e;
  --panel-head:#4a4a4a;
  --body-bg:#f1f1f1;
  --icon:#5b6f85;
}
*{box-sizing:border-box;margin:0;padding:0}
html,body{width:1200px;height:1080px;overflow:hidden}
body{font-family:"Open Sans",Arial,sans-serif;color:var(--ink);background:#fff;position:relative}
.top-strip{position:absolute;left:0;top:0;width:1200px;height:7px;background:#3a3a3a}
.header{position:absolute;left:0;top:7px;width:1200px;height:98px;background:#fff}
.brand{position:absolute;left:120px;top:30px;display:flex;align-items:center;gap:12px}
.brand-dot{width:40px;height:40px;border-radius:50%;background:var(--blue)}
.brand-name{font-family:"Montserrat",sans-serif;font-weight:700;font-size:36px;color:var(--blue)}
.utility{position:absolute;left:898px;top:-7px;display:flex;gap:6px}
.utility a{display:flex;align-items:center;gap:8px;height:30px;padding:0 16px;background:#3d3d3d;color:#fff;font-size:12px;text-decoration:none;border-radius:0 0 4px 4px}
.utility svg{width:14px;height:14px}
.contact-mail{position:absolute;right:120px;top:33px;font-size:12px;color:var(--muted);display:flex;align-items:center;gap:6px}
.social{display:flex;gap:5px}
.social span{width:24px;height:24px;background:var(--icon);display:block}
.header .social{position:absolute;right:120px;top:53px}
.nav{position:absolute;left:0;top:105px;width:1200px;height:42px;background:var(--blue)}
.nav ul{list-style:none;position:absolute;left:120px;top:0;display:flex;height:42px}
.nav li{height:42px;display:flex;align-items:center;padding:0 16px;color:#fff;font-family:"Montserrat",sans-serif;font-size:17px;border-right:1px solid rgba(255,255,255,.25)}
.nav li:last-child{border-right:0}
.nav li.active{background:var(--orange)}
.search{position:absolute;left:864px;top:8px;width:216px;height:26px;background:#fff;border:1px solid #d8d8d8;font-size:12px;font-style:italic;color:#999;padding:5px 10px}
.search svg{position:absolute;right:8px;top:6px;width:12px;height:12px}
.hero{position:absolute;left:0;top:147px;width:1200px;height:384px;background:linear-gradient(90deg,#ececec 0%,#f8f8f8 45%,#e6e6e6 100%)}
.hero-arrow{position:absolute;top:166px;width:40px;height:40px;border-radius:50%;background:#9a9a9a;display:flex;align-items:center;justify-content:center}
.hero-arrow svg{width:14px;height:14px}
.hero-title{position:absolute;left:140px;top:78px;font-family:"Montserrat",sans-serif;font-weight:700;font-size:38px;color:#4a4a4a;letter-spacing:-.5px}
.hero-title em{font-style:normal;color:var(--blue)}
.hero-copy{position:absolute;left:120px;top:134px;width:510px;font-size:14.5px;line-height:20px;color:#8a8a8a}
.btn-green{position:absolute;left:118px;top:254px;width:163px;height:43px;background:linear-gradient(#8fc126,var(--green-dark));border-radius:3px;color:#fff;font-family:"Montserrat",sans-serif;font-weight:700;font-size:19px;display:flex;align-items:center;justify-content:center;gap:10px}
.call{position:absolute;left:300px;top:248px;font-family:"Montserrat",sans-serif;font-weight:700;line-height:25px}
.call .label{color:#8db42a;font-size:22px}
.call .phone{color:var(--blue);font-size:22px}
.signup{position:absolute;left:706px;top:31px;width:374px;height:333px;background:#fff;border-radius:5px;box-shadow:0 1px 4px rgba(0,0,0,.15);overflow:hidden}
.signup h2{height:52px;background:var(--panel-head);color:#fff;font-family:"Montserrat",sans-serif;font-weight:600;font-size:23px;padding:12px 22px}
.field{position:absolute;left:24px;display:flex;align-items:center;width:330px}
.field label{width:125px;font-size:14px;color:#444}
.field .input{width:200px;height:37px;border:1px solid #ddd;border-radius:2px;background:#fff;position:relative}
.field .input::after{content:"";position:absolute;right:0;top:0;border-style:solid;border-width:0 12px 12px 0;border-color:transparent #3d3d3d transparent transparent}
.field .input.focus{border-color:var(--orange)}
.field .input.focus::after{border-color:transparent var(--orange) transparent transparent}
.submit{position:absolute;left:148px;top:280px;width:116px;height:34px;background:linear-gradient(#8fc126,var(--green-dark));border-radius:3px;color:#fff;font-family:"Montserrat",sans-serif;font-weight:700;font-size:18px;display:flex;align-items:center;justify-content:center}
.features{position:absolute;left:0;top:531px;width:1200px;height:439px;background:var(--body-bg)}
.card{position:absolute;top:47px;width:294px;height:334px;background:#fff;box-shadow:0 1px 4px rgba(0,0,0,.12);padding:20px}
.card.active{background:linear-gradient(#fff,#ececec)}
.card-media{position:relative;width:254px;height:154px}
.card-media .caption{position:absolute;left:0;bottom:0;width:100%;height:40px;background:rgba(0,0,0,.35);color:#fff;font-family:"Montserrat",sans-serif;font-weight:600;font-size:16px;padding:10px 16px}
.card p{margin-top:18px;font-size:12.5px;line-height:16px;color:#9a9a9a;text-align:justify}
.card.active p{color:#444}
.card .more{margin-top:14px;display:inline-flex;align-items:center;gap:8px;height:29px;padding:0 14px;border:1px solid #ccc;border-radius:3px;background:#f1f1f1;font-size:13px;color:#666}
.card.active .more{background:var(--blue);border-color:var(--blue-dark);color:#fff}
.footer{position:absolute;left:0;top:970px;width:1200px;height:110px;background:var(--charcoal)}
.footer ul{list-style:none;position:absolute;left:118px;top:27px;display:flex;gap:22px}
.footer li{color:#eee;font-size:13px}
.footer .social{position:absolute;right:120px;top:24px}
.footer .rule{position:absolute;left:0;top:69px;width:1200px;height:1px;background:#444}
.footer .legal{position:absolute;left:120px;top:84px;font-size:11px;color:#888}
</style>
</head>
<body>
<div class="top-strip"></div>

<header class="header">
  <div class="brand"><span class="brand-dot"></span><span class="brand-name">Tallyvane</span></div>
  <div class="utility">
    <a href="#"><svg viewBox="0 0 14 14"><circle cx="7" cy="4" r="3" fill="#fff"/><path d="M1 14c0-4 3-6 6-6s6 2 6 6z" fill="#fff"/></svg>Sign In</a>
    <a href="#"><svg viewBox="0 0 14 14"><circle cx="7" cy="7" r="7" fill="#fff"/><text x="7" y="11" font-size="10" text-anchor="middle" fill="#3d3d3d" font-family="Arial">?</text></svg>Help</a>
  </div>
  <div class="contact-mail"><svg width="12" height="9" viewBox="0 0 12 9"><rect x=".5" y=".5" width="11" height="8" fill="none" stroke="#999"/><path d="M.5 .5l5.5 4.5 5.5-4.5" fill="none" stroke="#999"/></svg>info@tallyvane.com</div>
  <div class="social" aria-label="Social media links"><span></span><span></span><span></span><span></span></div>
</header>

<nav class="nav">
  <ul>
    <li>Home</li><li>About Us</li><li>Team</li><li class="active">Customers</li><li>Jobs</li><li>Contact Us</li><li>Sign UP</li>
  </ul>
  <div class="search">Search here..<svg viewBox="0 0 12 12"><circle cx="5" cy="5" r="3.5" fill="none" stroke="#999" stroke-width="1.5"/><path d="M8 8l3 3" stroke="#999" stroke-width="1.5"/></svg></div>
</nav>

<section class="hero" role="img" aria-label="Bright white office interior with large windows, softly blurred">
  <div class="hero-arrow" style="left:28px"><svg viewBox="0 0 14 14"><path d="M9 2L4 7l5 5" fill="none" stroke="#fff" stroke-width="2.5"/></svg></div>
  <div class="hero-arrow" style="left:1130px"><svg viewBox="0 0 14 14"><path d="M5 2l5 5-5 5" fill="none" stroke="#fff" stroke-width="2.5"/></svg></div>
  <h1 class="hero-title"><em>Create Surveys.</em> Get Answers.</h1>
  <p class="hero-copy">Lorem Ipsum is simply dummy text of the printing and typesetting industry. Lorem Ipsum has been the industry's standard dummy text ever since the 1500s, when an unknown printer took a galley of type and scrambled it to make a type specimen book.</p>
  <div class="btn-green">Read More <svg width="16" height="16" viewBox="0 0 16 16"><circle cx="8" cy="8" r="8" fill="#fff"/><path d="M6.5 4.5L10 8l-3.5 3.5" fill="none" stroke="#6a9a14" stroke-width="2"/></svg></div>
  <div class="call"><div class="label">Call Us:</div><div class="phone">(555) 014-2270</div></div>

  <form class="signup">
    <h2>Sign Up - It's Free!</h2>
    <div class="field" style="top:71px"><label>First Name</label><div class="input focus"></div></div>
    <div class="field" style="top:136px"><label>Last Name</label><div class="input"></div></div>
    <div class="field" style="top:197px"><label>Email Address</label><div class="input"></div></div>
    <div class="submit">Submit</div>
  </form>
</section>

<section class="features">
  <article class="card" style="left:120px">
    <div class="card-media" role="img" aria-label="Photo of colleagues reviewing data on a computer screen" style="background:linear-gradient(135deg,#c9b59a,#8a7660 60%,#4d4a46)"><div class="caption">Fresh Data</div></div>
    <p>Lorem Ipsum is simply dummy text of the printing and typesetting industry. Lorem Ipsum has been the industry's standard dummy text ever since the when an unknown printer took a galley.</p>
    <div class="more">Read More <svg width="12" height="12" viewBox="0 0 12 12"><circle cx="6" cy="6" r="6" fill="#777"/><path d="M5 3.5L7.5 6 5 8.5" fill="none" stroke="#fff" stroke-width="1.5"/></svg></div>
  </article>
  <article class="card active" style="left:453px">
    <div class="card-media" role="img" aria-label="Photo of a business team meeting around a table with laptops" style="background:linear-gradient(135deg,#6b5a4a,#a08870 50%,#3a3a3a)"><div class="caption">Sales Intelligence</div></div>
    <p>Lorem Ipsum is simply dummy text of the printing and typesetting industry. Lorem Ipsum has been the industry's standard dummy text ever since the when an unknown printer took a galley.</p>
    <div class="more">Read More <svg width="12" height="12" viewBox="0 0 12 12"><circle cx="6" cy="6" r="6" fill="#fff"/><path d="M5 3.5L7.5 6 5 8.5" fill="none" stroke="#1a8fe8" stroke-width="1.5"/></svg></div>
  </article>
  <article class="card" style="left:785px">
    <div class="card-media" role="img" aria-label="Illustration of rising blue bar graph with an orange upward arrow" style="background:linear-gradient(135deg,#f4f4f4,#bcd9ef 55%,#2f7fc0)"><div class="caption">Increased Bottomline</div></div>
    <p>Lorem Ipsum is simply dummy text of the printing and typesetting industry. Lorem Ipsum has been the industry's standard dummy text ever since the when an unknown printer took a galley.</p>
    <div class="more">Read More <svg width="12" height="12" viewBox="0 0 12 12"><circle cx="6" cy="6" r="6" fill="#777"/><path d="M5 3.5L7.5 6 5 8.5" fill="none" stroke="#fff" stroke-width="1.5"/></svg></div>
  </article>
</section>

<footer class="footer">
  <ul><li>Home</li><li>About Us</li><li>Team</li><li>Customers</li><li>Jobs</li><li>Contact Us</li><li>Sign UP</li></ul>
  <div class="social" aria-label="Social media links"><span></span><span></span><span></span><span></span></div>
  <div class="rule"></div>
  <div class="legal">©2013 Tallyvane Corporation.&nbsp; All Rights Reserved</div>
</footer>
</body>
</html>
```